Header image for law blog

I need a header image for my blog at www.prairiegavelwire.net.

The colors would match the current site. It would say: "Gavel Wire: Estate Planning and Real Estate on the Open Prairie."

I also want to add in smaller type "Law Office of Ned Farrow 555 014 2738 ned@farrowq.com."

The theme maker suggests a header size of 1600 × 230 pixels.

```html
<!DOCTYPE html>
<html lang="en">
<head>
<meta charset="utf-8">
<title>FHA 90-day seasoning requirement is back for flips</title>
<link href="https://fonts.googleapis.com/css2?family=Arvo:wght@700&family=Bitter:wght@400;700&family=Source+Sans+3:ital,wght@0,300;0,400;0,700;1,300&display=swap" rel="stylesheet">
<style>
  :root{
    --accent:#d9481c;
    --link:#bc360a;
    --ink:#141412;
    --text:#222;
    --band:#f7f5e7;
    --widget:#f5f3e6;
    --rule:#e6e3d3;
    --field:#fff;
    --field-border:#c8c4b0;
    --button:#e05d22;
    --button-dark:#b93207;
  }
  *{box-sizing:border-box;margin:0;padding:0}
  html,body{width:1200px;height:1000px;overflow:hidden;background:#fff}
  body{font-family:"Source Sans 3","Source Sans Pro",sans-serif;color:var(--text);position:relative}
  .page-edge{position:absolute;left:18px;top:0;width:1px;height:1000px;background:var(--rule)}
  .site-header{position:absolute;left:18px;top:0;width:1182px;height:228px;overflow:hidden}
  .header-photo{position:absolute;inset:0;background:linear-gradient(180deg,#d9d3c4 0%,#ccc6b8 45%,#a9a59c 80%,#8e8c88 100%)}
  .header-figure{position:absolute;left:30px;top:0;width:300px;height:228px;background:linear-gradient(180deg,rgba(255,255,255,.35),rgba(60,50,45,.35));border-radius:40px 40px 0 0}
  .header-text{position:absolute;left:352px;top:24px}
  .site-title{font-family:"Bitter",Georgia,serif;font-weight:700;font-size:54px;line-height:1;color:var(--accent);letter-spacing:1px}
  .site-tagline{font-family:"Bitter",Georgia,serif;font-weight:700;font-size:26px;line-height:1.2;color:var(--ink);margin-top:10px;white-space:nowrap}
  .header-rule{position:absolute;left:352px;top:123px;width:830px;height:2px;background:var(--accent)}
  .office{position:absolute;left:352px;top:132px;font-family:"Arvo",Georgia,serif;font-weight:700}
  .office-label{font-size:18px;color:var(--ink)}
  .office-line{display:flex;align-items:center;gap:8px;font-size:19px;color:var(--accent);margin-top:2px;white-space:nowrap}
  .office-line svg{flex:none}
  .office-line .gap{width:12px}
  .nav-bar{position:absolute;left:18px;top:228px;width:1182px;height:47px;background:var(--band)}
  .nav-bar a{position:absolute;top:14px;font-size:15px;color:var(--ink);text-decoration:none}
  .entry{position:absolute;left:358px;top:316px;width:605px}
  .entry-title{font-family:"Bitter",Georgia,serif;font-weight:400;font-size:48px;line-height:61px;color:var(--ink)}
  .entry-meta{margin-top:8px;font-size:13px;color:var(--link);display:flex;gap:18px;align-items:center}
  .entry-meta span{display:flex;align-items:center;gap:4px}
  .entry-content{margin-top:33px;font-size:15px;line-height:24px;color:var(--text)}
  .entry-content p{margin-bottom:24px}
  .entry-content p.tight{margin-bottom:0}
  .entry-content a{color:var(--link);text-decoration:none}
  .share{font-weight:700;font-size:15px;color:var(--ink);margin-top:-7px}
  .share-icons{display:flex;gap:5px;margin-top:7px}
  .share-icons i{width:16px;height:16px;display:block;border-radius:2px}
  .sidebar{position:absolute;left:1038px;top:315px;width:200px}
  .widget{background:var(--widget);padding:20px 20px 20px}
  .widget + .widget{margin-top:24px}
  .widget-title{font-size:20px;font-weight:300;font-style:italic;color:var(--ink);white-space:nowrap;margin-bottom:12px;line-height:26px}
  .widget a{display:block;font-size:13px;color:var(--link);text-decoration:none;line-height:31px;white-space:nowrap}
  .widget p{font-size:13px;line-height:17px;color:var(--ink);white-space:nowrap}
  .field-label{font-size:13px;color:var(--ink);margin-top:22px;margin-bottom:7px}
  .newsletter .field-label:first-of-type{margin-top:20px}
  .field{height:32px;background:var(--field);border:2px solid var(--field-border);border-radius:2px}
  .note{font-size:13px;color:var(--ink);margin-top:18px}
  .subscribe{margin:22px 0 0 26px;height:42px;background:linear-gradient(var(--button),var(--button-dark));color:#fff;font-size:14px;font-weight:700;padding:11px 0 0 74px;border-radius:2px;white-space:nowrap}
</style>
</head>
<body>
<div class="page-edge"></div>

<header class="site-header">
  <div class="header-photo" role="img" aria-label="Hazy city skyline seen from above at dawn"></div>
  <div class="header-figure" role="img" aria-label="Businessman in white shirt and tie standing with arms spread wide, holding his jacket"></div>
  <div class="header-text">
    <h1 class="site-title">GAVEL WIRE:</h1>
    <p class="site-tagline">Estate Planning and Real Estate on the Open Prairie</p>
  </div>
  <div class="header-rule"></div>
  <div class="office">
    <div class="office-label">Law Office of</div>
    <div class="office-line">
      <span>NED FARROW</span><span class="gap"></span>
      <svg width="18" height="20" viewBox="0 0 18 20"><rect x="1" y="1" width="16" height="18" rx="2" fill="#141412"/><path d="M6 5c-1 1-1 3 1 6s4 4 5 3l-1-2-2 1c-1-1-2-2-2-4l1-1z" fill="#fff"/></svg>
      <span>555 014 2738</span><span class="gap"></span>
      <svg width="22" height="16" viewBox="0 0 22 16"><rect x="1" y="1" width="20" height="14" fill="#141412"/><path d="M2 2l9 7 9-7" stroke="#fff" stroke-width="1.5" fill="none"/></svg>
      <span>ned@farrowq.com</span>
    </div>
  </div>
</header>

<nav class="nav-bar">
  <a style="left:279px">About us</a>
  <a style="left:375px">Archives</a>
</nav>

<article class="entry">
  <h2 class="entry-title">FHA 90-day seasoning requirement is back for flips</h2>
  <div class="entry-meta">
    <span><svg width="11" height="11" viewBox="0 0 12 12"><circle cx="6" cy="6" r="5" fill="none" stroke="currentColor" stroke-width="1.4"/><path d="M6 3v3h2" stroke="currentColor" stroke-width="1.4" fill="none"/></svg>March 1, 2015</span>
    <span><svg width="12" height="10" viewBox="0 0 12 10"><path d="M0 1h4l1 1h7v8H0z" fill="currentColor"/></svg>Mortgages, Real Estate-Purchases</span>
    <span><svg width="10" height="11" viewBox="0 0 10 11"><circle cx="5" cy="3" r="2.6" fill="currentColor"/><path d="M0 11c0-4 2-5 5-5s5 1 5 5z" fill="currentColor"/></svg>nfarrow</span>
  </div>
  <div class="entry-content">
    <p>Be careful if you are buying a property that the seller is trying to flip. WIth a flip, the seller buys a distressed or foreclosed property, fixes it up and then quickly resells it. If you are getting an FHA mortgage to buy a&nbsp; property being flipped, you will not be able to <a>sign a contrac</a>t to purchase the property until 90 days after the seller has owned the property.</p>
    <p class="tight">The 90 day time period is measured from the date the seller acquired the property (closed on the property)&nbsp; to the dale the seller signs a contract with the new FHA buyer.</p>
    <p class="tight">The purpose of this FHA <a>“seasoning”</a> rule is to prevent sellers from acquiring a property, doing cosmetic repairs and then reselling it at an inflated price. For the past few years, during the depressed real estate market, FHA waived this rule and allowed the buyer to sign the contract earlier than 90 days, but that changed on January 1, 2015.</p>
    <p class="tight">But now, FHA is back to enforcing the seasoning requirement.</p>
    <p>I have also found that many lenders will require two appraisals to be done if the buyer is buying a flipped property. This will often delay closing because the parties have to wait for the second appraisal.</p>
  </div>
  <div class="share">Share and Enjoy:</div>
  <div class="share-icons">
    <i style="background:#9aa"></i><i style="background:#bbb"></i><i style="background:#779"></i><i style="background:#5a7ab8"></i><i style="background:#5d9"></i><i style="background:#3b82b8"></i><i style="background:#4a9"></i><i style="background:#8cd"></i><i style="background:#99a"></i><i style="background:#6c6"></i><i style="background:#ec9"></i>
  </div>
</article>

<aside class="sidebar">
  <section class="widget" style="height:137px">
    <h3 class="widget-title">Set an appointment</h3>
    <a>Schedule a phone appointment</a>
    <a>Schedule an office appointment</a>
  </section>
  <section class="widget newsletter" style="height:441px">
    <h3 class="widget-title">Sign up for the Newsletter</h3>
    <p>Give us your email and we'll send you our</p>
    <p>newsletter every month</p>
    <div class="field-label">Email Address*</div><div class="field"></div>
    <div class="field-label">First Name</div><div class="field"></div>
    <div class="field-label">Last Name</div><div class="field"></div>
    <div class="note">* = required field</div>
    <div class="subscribe">Subscribe</div>
  </section>
  <section class="widget" style="height:80px">
    <h3 class="widget-title">Categories</h3>
  </section>
</aside>
</body>
</html>
```